New Corporate website more focused on funnel and great design

Our company, Bold Harbor needs a new website to look like it's from 2021. We work with large businesses in the corporte world and need to reflect that we are professional, focused on our clients, and trsutworthy. It should include some/most of the components from our current site: boldharbor.com but should focus more about getting people to optin to out free downloads, which can be found on this page: https://www.boldharbor.com/get-started-with-a-prep-session/ and this page: https://www.boldharbor.com/team-onboarding/

Our new website should do a better job at explaining what we do, who we serve, and how we fix their problems of onboarding new leaders. Feel free to use dummy text if you are not sure what to put in for certain sections. I also would like to point out that most of the audiance is older, so we don't need anything too younge and flashy, or that is hard it use. it should have big clear fonts, plently of contrast, and work well for poeple who are not good at using the internet. Please use the colors of the logo, and you can add another color or two if you think it's fits

Industry/Entity Type

business consulting

Number of Pages Required

2 page

Font styles to use
Sans Serif

Requirements
Must have
• corporate feel, look professional, focus on getting new leads
Should not have
• cute or children feel

```html
<!DOCTYPE html>
<html lang="en">
<head>
<meta charset="utf-8">
<title>Bold Harbor — Leading With Clarity</title>
<link href="https://fonts.googleapis.com/css2?family=Roboto:wght@300;400;500;700&display=swap" rel="stylesheet">
<style>
:root{
  --blue:#14508f;
  --blue-title:#1b5c98;
  --orange:#ee7d30;
  --dark:#222222;
  --footer:#262626;
  --text:#555b61;
  --muted:#8a8f94;
  --light:#f5f5f5;
  --white:#ffffff;
}
*{box-sizing:border-box;margin:0;padding:0}
html,body{width:1200px;height:3859px;overflow:hidden}
body{font-family:'Roboto',sans-serif;color:var(--text);background:var(--white);position:relative}
section,header,footer,.topbar{position:relative;width:1200px;overflow:hidden}
.abs{position:absolute}
.btn{position:absolute;display:flex;align-items:center;justify-content:center;gap:10px;font-size:11px;font-weight:700;letter-spacing:.3px;text-transform:uppercase;text-decoration:none}
.btn-orange{background:var(--orange);color:var(--white)}
.btn-outline{border:2px solid var(--white);color:var(--white)}
.center{left:0;right:0;text-align:center}
.eyebrow{font-size:19px;color:#2a2a2a;font-weight:400;text-transform:uppercase}
.section-title{font-size:31px;color:var(--blue-title);font-weight:500}

/* top bar */
.topbar{height:37px;background:var(--dark);color:#ccc}
.topbar .call{position:absolute;right:135px;top:10px;font-size:11px;display:flex;align-items:center;gap:8px}
.topbar .call strong{color:#fff;font-size:14px;font-weight:400}

/* header */
header{height:84px;background:#fff}
.brand{position:absolute;left:135px;top:22px;display:flex;align-items:center;gap:12px}
.brand-square{width:40px;height:40px;background:var(--blue)}
.brand-name{font-size:27px;font-weight:500;color:var(--blue)}
.nav{position:absolute;right:135px;top:34px;display:flex;gap:31px;font-size:12.5px;color:#444}

/* hero */
.hero{height:468px;background:linear-gradient(90deg,#e3eef0 0%,#e8f1f2 55%,#dfe9ec 100%)}
.hero-photo{position:absolute;left:700px;top:0;width:500px;height:468px;background:linear-gradient(90deg,rgba(226,237,240,0) 0%,#c9d7dd 30%,#a9bcc6 60%,#7f8f98 100%)}
.hero h1{position:absolute;left:138px;top:115px;font-size:52px;font-weight:500;color:var(--blue-title)}
.hero p{position:absolute;left:139px;top:180px;width:600px;font-size:24px;line-height:34px;color:#2b2b2b;font-weight:400}
.hero .btn{left:138px;top:297px;width:128px;height:33px}

/* about */
.about{height:254px;background:#fff}
.about .eyebrow{position:absolute;top:56px}
.about .section-title{position:absolute;top:78px}
.about p{position:absolute;left:180px;width:840px;top:119px;font-size:13px;line-height:24px;color:#666;text-align:center}

/* services */
.services{height:337px;display:flex}
.service{position:relative;width:400px;height:337px;color:#fff}
.service.dark{background:var(--dark)}
.service.blue{background:var(--blue)}
.service.orange{background:var(--orange)}
.service .icon{position:absolute;left:72px;top:52px}
.service h3{position:absolute;left:72px;top:98px;font-size:16px;font-weight:700}
.service h4{position:absolute;left:72px;top:133px;font-size:12.5px;font-weight:700}
.service p{position:absolute;left:72px;top:152px;width:270px;font-size:11.3px;line-height:15.5px}
.service .btn{left:72px;top:253px;width:145px;height:34px}

/* insights */
.insights{height:806px;background:var(--light)}
.insights .eyebrow{position:absolute;top:72px}
.insights .section-title{position:absolute;top:93px}
.insights .sub{position:absolute;top:138px;font-size:12.5px;color:#555}
.rule{position:absolute;left:562px;top:172px;width:78px;height:3px;background:var(--orange)}
.book-panel{position:absolute;left:135px;top:219px;width:295px;height:521px;background:var(--blue)}
.bubble{position:absolute;left:170px;top:40px;width:106px;height:58px;border:2px solid #fff;border-radius:50%;color:#fff;font-size:9.5px;font-weight:500;text-align:center;padding-top:16px;line-height:12px}
.book-cover{position:absolute;left:54px;top:128px;width:189px;height:287px;background:linear-gradient(180deg,#f3f1ee 0%,#e9e6e1 70%,#d9d5cf 100%);box-shadow:0 3px 10px rgba(0,0,0,.35)}
.book-panel .btn{left:45px;top:468px;width:205px;height:33px}
.post{position:absolute;background:#fff;height:209px}
.post .photo{position:absolute;top:0;width:228px;height:209px}
.post .body{position:absolute;top:20px;width:315px}
.post h5{font-size:10.5px;font-weight:500;color:#2b2b2b;text-transform:uppercase}
.post .meta{font-size:10.5px;margin-top:12px;color:#777}
.post .meta b{color:var(--blue-title);font-weight:400}
.post .meta span{margin:0 10px;color:#aaa}
.post p{font-size:12px;line-height:18px;color:#666;margin-top:10px}
.post .more{margin-top:16px;font-size:10.5px;font-weight:700;color:var(--orange);display:flex;align-items:center;gap:10px}
.blog-link{position:absolute;left:672px;top:692px;font-size:11px;font-weight:700;color:var(--orange);text-decoration:underline}

/* download band */
.download{height:167px;background:var(--blue);color:#fff}
.dl-brand{position:absolute;left:158px;top:24px;width:122px;text-align:center}
.dl-brand .w{font-size:18px;font-weight:700;letter-spacing:.5px}
.dl-brand .sq{width:36px;height:36px;background:#fff;margin:6px auto 4px}
.dl-brand .t{font-size:15px;font-weight:700;line-height:16px}
.field{position:absolute;background:#fff;border-radius:3px;font-size:12px;color:#444;padding-left:15px;display:flex;align-items:center}
.download .btn{top:66px;left:694px;width:130px;height:35px;border-radius:3px;font-size:12px}
.dl-stat{position:absolute;left:846px;top:69px;width:84px;font-size:11px;line-height:15px;text-align:center}
.ring{position:absolute;left:944px;top:25px;width:120px;height:120px;border:3px solid #fff;border-radius:50%;display:flex;align-items:center;justify-content:center;font-size:46px;font-weight:400}

/* testimonials */
.clients{height:723px;background:#fff}
.clients .eyebrow{position:absolute;top:72px}
.clients .section-title{position:absolute;top:93px}
.quote-card{position:absolute;left:307px;top:201px;width:586px;height:141px;border:1px solid #e6e6e6}
.avatar{position:absolute;left:567px;top:174px;width:66px;height:66px;border-radius:50%;background:linear-gradient(180deg,#d8dde2,#9aa4ad);border:4px solid #fff;box-shadow:0 0 0 1px #e2e2e2}
.quote{position:absolute;top:256px;font-size:12.5px;line-height:19px;color:#666}
.quote-name{position:absolute;top:304px;font-size:12.5px;font-weight:700;color:var(--blue-title)}
.dots{position:absolute;top:372px;left:578px;display:flex;gap:5px}
.dots i{width:7px;height:7px;border-radius:50%;background:#222}
.dots i.on{background:var(--orange)}
.divider{position:absolute;left:135px;top:438px;width:930px;height:1px;background:#e8e8e8}
.clients h3{position:absolute;top:466px;font-size:20px;font-weight:500;color:#222}
.client-row{position:absolute;left:305px;top:537px;width:590px;display:flex;justify-content:space-between;align-items:center}
.client{display:flex;align-items:center;gap:6px;font-size:19px;font-weight:500;color:#1e4f86}
.client .mk{width:14px;height:14px;background:var(--blue)}
.clients .btn{left:497px;top:622px;width:205px;height:33px}

/* contact */
.contact{height:534px;background:linear-gradient(180deg,#1a4f87 0%,#175193 50%,#134782 100%);color:#fff}
.contact .eyebrow{position:absolute;top:88px;color:#fff}
.contact .section-title{position:absolute;top:108px;color:#fff;font-weight:400}
.input{position:absolute;border:1px solid rgba(255,255,255,.85);border-radius:3px;font-size:12px;padding:12px 14px;color:#fff}
.contact .btn{left:548px;top:419px;width:105px;height:39px;border:1px solid #fff;border-radius:3px;color:#fff}

/* footer */
footer{height:449px;background:var(--footer);color:#9a9a9a}
.fcol{position:absolute;top:60px;width:217px}
.fcol h4{font-size:17px;font-weight:400;color:#fff}
.fcol .bar{width:46px;height:3px;background:var(--orange);margin-top:12px}
.fcol ul{list-style:none;margin-top:14px}
.fcol li{font-size:11px;height:31px;line-height:30px;border-bottom:1px solid #3a3a3a}
.fcol li:last-child{border-bottom:none}
.ci{display:flex;gap:12px;margin-top:16px;border-bottom:1px solid #3a3a3a;padding-bottom:12px}
.ci b{display:block;color:#fff;font-weight:400;font-size:11.5px;margin-bottom:4px}
.ci div{font-size:10.5px;line-height:16px}
.news p{font-size:10.5px;margin-top:18px}
.news .mail{margin-top:16px;height:34px;background:#fff;border-radius:3px;display:flex;align-items:center;justify-content:space-between;padding:0 12px;font-size:11px;color:#999}
.socials{display:flex;gap:14px;margin-top:14px}
.socials span{width:32px;height:32px;border:1px solid #777;border-radius:50%;display:flex;align-items:center;justify-content:center;font-size:8px;color:#bbb}
.fline{position:absolute;left:135px;top:388px;width:930px;height:1px;background:#444}
.copy{position:absolute;top:407px;font-size:10.5px}
</style>
</head>
<body>

<div class="topbar">
  <div class="call">
    <svg width="14" height="14" viewBox="0 0 24 24"><path fill="#ee7d30" d="M6.6 10.8c1.4 2.8 3.8 5.1 6.6 6.6l2.2-2.2c.3-.3.7-.4 1-.2 1.1.4 2.3.6 3.6.6.6 0 1 .4 1 1V20c0 .6-.4 1-1 1C10.6 21 3 13.4 3 4c0-.6.4-1 1-1h3.5c.6 0 1 .4 1 1 0 1.3.2 2.5.6 3.6.1.3 0 .7-.2 1z"/></svg>
    <span>Call Us Today : <strong>+1 555.014.2290</strong></span>
  </div>
</div>

<header>
  <div class="brand"><span class="brand-square"></span><span class="brand-name">Bold Harbor</span></div>
  <nav class="nav"><span>Who we are</span><span>What We Do</span><span>Resources</span><span>Our Clients</span><span>Blog</span><span>Contact</span></nav>
</header>

<section class="hero">
  <div class="hero-photo" role="img" aria-label="Photo of smiling business leaders gathered around a tablet in a bright office"></div>
  <h1>Bold Harbor</h1>
  <p>We know, through our personal experiences gained as leaders, that the first 100 days in a critical transition are a crucible of leadership.</p>
  <a class="btn btn-orange">Contact us</a>
</section>

<section class="about">
  <div class="eyebrow abs center">About us</div>
  <div class="section-title abs center">Bold Harbor</div>
  <p>Accelerate Business Performance During Critical Leadership Transitions There are many variations of passages of Lorem Ipsum available, but the majority have suffered alteration in some form, by injected humour, or randomised words which don't look even slightly believable. There are many variations of passages of Lorem Ipsum available, but the majority have suffered alteration in some form, by injected humour, or randomised words which don't look even slightly believable.</p>
</section>

<section class="services">
  <div class="service dark">
    <svg class="icon" width="40" height="34" viewBox="0 0 40 34" fill="#fff"><circle cx="8" cy="6" r="3.5"/><circle cx="20" cy="5" r="4"/><circle cx="32" cy="6" r="3.5"/><path d="M2 32V15c0-3 2-5 6-5s6 2 6 5v17zM14 32V14c0-3 2-5 6-5s6 2 6 5v18zM26 32V15c0-3 2-5 6-5s6 2 6 5v17z"/></svg>
    <h3>Executive Onboarding</h3>
    <h4>40% of new leaders fail</h4>
    <p>For executive leaders taking on new roles, the Bold Harbor 100-Day Action Plan process prepares leaders before the start, speeds up assimilation, sets direction, builds the team, accelerates momentum, and delivers results.</p>
    <a class="btn btn-outline">Learn more <svg width="22" height="10" viewBox="0 0 22 10"><path d="M0 5h20M15 1l5 4-5 4" stroke="#fff" stroke-width="1.6" fill="none"/></svg></a>
  </div>
  <div class="service blue">
    <svg class="icon" width="36" height="34" viewBox="0 0 36 34" fill="none" stroke="#fff" stroke-width="1.6"><circle cx="9" cy="7" r="4"/><circle cx="27" cy="7" r="4"/><circle cx="18" cy="18" r="4"/><path d="M2 32c0-5 3-8 7-8M34 32c0-5-3-8-7-8M10 32c0-4 3-7 8-7s8 3 8 7"/></svg>
    <h3>Team Onboarding</h3>
    <h4>80% of M&amp;A fail to boost returns</h4>
    <p>For leaders integrating teams post acquisition or re-organization, the Bold Harbor 100 Day Action Plan process gets all players on board with the change and accelerates achievement of cultural and business integration goals.</p>
    <a class="btn btn-outline">Learn more <svg width="22" height="10" viewBox="0 0 22 10"><path d="M0 5h20M15 1l5 4-5 4" stroke="#fff" stroke-width="1.6" fill="none"/></svg></a>
  </div>
  <div class="service orange">
    <svg class="icon" width="36" height="36" viewBox="0 0 36 36" fill="none" stroke="#fff" stroke-width="1.6"><path d="M34 2C24 4 14 12 8 22l6 6c10-6 18-16 20-26zM8 22l-6 2 4 4M14 28l-2 6-4-4M20 10l6 6"/></svg>
    <h3>Acceleration &amp; Restart</h3>
    <h4>70% of transformations fall short</h4>
    <p>For executives leading through a strategic point of inflection or reinvigorating a stalled team, Bold Harbor programs define the from-to challenge, kickstart a change process and deliver results that stick.</p>
    <a class="btn btn-outline">Learn more <svg width="22" height="10" viewBox="0 0 22 10"><path d="M0 5h20M15 1l5 4-5 4" stroke="#fff" stroke-width="1.6" fill="none"/></svg></a>
  </div>
</section>

<section class="insights">
  <div class="eyebrow abs center">Insights</div>
  <div class="section-title abs center">Books and Blogs</div>
  <div class="sub abs center">Books, news, research, client success stories, opinions, and perspectives on Bold Harbor</div>
  <div class="rule"></div>

  <div class="book-panel">
    <div class="bubble">90% of our<br>Clients Succeed</div>
    <div class="book-cover" role="img" aria-label="Cover of the 100-day action plan book for new leaders"></div>
    <a class="btn btn-orange">Browse all of our book</a>
  </div>

  <article class="post" style="left:454px;top:219px;width:611px">
    <div class="body" style="left:23px">
      <h5>Why Norvale's new CFO should fail, but won't</h5>
      <div class="meta"><b>BY MARTIN ELLERY</b><span>|</span>MAY 17, 2021</div>
      <p>On the one hand, it looks like everything is stacked against her. Almost any set of assumptions plugged into our onboarding risk calculator suggests she should run, not walk away from this situation.</p>
      <div class="more">READ MORE <svg width="22" height="10" viewBox="0 0 22 10"><path d="M0 5h20M15 1l5 4-5 4" stroke="#ee7d30" stroke-width="1.6" fill="none"/></svg></div>
    </div>
    <div class="photo" style="left:383px;background:linear-gradient(135deg,#cfcfcf,#6f6f6f 60%,#3c3c3c)" role="img" aria-label="Black and white archival photo of two men shaking hands"></div>
  </article>

  <article class="post" style="left:454px;top:452px;width:611px">
    <div class="photo" style="left:0;background:linear-gradient(135deg,#8a6a4e,#4a3a34 50%,#2a2a2e)" role="img" aria-label="Photo of senior executives seated at a hearing table"></div>
    <div class="body" style="left:249px">
      <h5>Why 'thank you' beats 'yes' in strategic selling</h5>
      <div class="meta"><b>BY MARTIN ELLERY</b><span>|</span>MAY 17, 2021</div>
      <p>On the one hand, it looks like everything is stacked against her. Almost any set of assumptions plugged into our onboarding risk calculator suggests she should run, not walk away from this situation.</p>
      <div class="more">READ MORE <svg width="22" height="10" viewBox="0 0 22 10"><path d="M0 5h20M15 1l5 4-5 4" stroke="#ee7d30" stroke-width="1.6" fill="none"/></svg></div>
    </div>
  </article>
  <a class="blog-link">READ MORE LEADERSHIP BLOGS</a>
</section>

<section class="download">
  <div class="dl-brand"><div class="w">DOWNLOAD</div><div class="sq"></div><div class="t">100 Day Action<br>Plan Process</div></div>
  <div class="field" style="left:318px;top:66px;width:182px;height:35px">Name</div>
  <div class="field" style="left:506px;top:66px;width:183px;height:35px">Email</div>
  <a class="btn btn-orange">Download now</a>
  <div class="dl-stat">90% of our clients succeed</div>
  <div class="ring">90%</div>
</section>

<section class="clients">
  <div class="eyebrow abs center">Insights</div>
  <div class="section-title abs center">What Our Clients Say</div>
  <div class="quote-card"></div>
  <div class="avatar" role="img" aria-label="Portrait of the client quoted"></div>
  <div class="quote abs center">Somewhere right now, there is a first time CEO out there, not working with<br>Bold Harbor, not following their 100-Day Action Plan, and I am worried for them.</div>
  <div class="quote-name abs center">Peter Holm, CEO Keystone Integrated Systems</div>
  <div class="dots"><i class="on"></i><i></i><i></i><i></i></div>
  <div class="divider"></div>
  <h3 class="abs center">Our Top 10 Clients Have Used Us Over 180 Times</h3>
  <div class="client-row">
    <span class="client"><span class="mk"></span>Cloudvault</span>
    <span class="client">Ridgeway</span>
    <span class="client">Stonebridge</span>
    <span class="client"><span class="mk"></span>Vantage</span>
    <span class="client">Brightline</span>
  </div>
  <a class="btn btn-orange">See our worldwide clients</a>
</section>

<section class="contact">
  <div class="eyebrow abs center">Comunication</div>
  <div class="section-title abs center">Speak to One of Our Partners Today</div>
  <div class="input" style="left:349px;top:189px;width:235px;height:35px">First Name</div>
  <div class="input" style="left:616px;top:189px;width:235px;height:35px">Second Name</div>
  <div class="input" style="left:349px;top:241px;width:235px;height:35px">Email Address</div>
  <div class="input" style="left:616px;top:241px;width:235px;height:35px">Phone Number</div>
  <div class="input" style="left:349px;top:294px;width:502px;height:87px">Message</div>
  <a class="btn">Send</a>
</section>

<footer>
  <div class="fcol" style="left:135px">
    <h4>What We Do</h4><div class="bar"></div>
    <ul><li>Executive Onboarding</li><li>Team Onboarding</li><li>Acceleration &amp; Restart</li><li>Case Studies</li></ul>
  </div>
  <div class="fcol" style="left:372px">
    <h4>Quick Links</h4><div class="bar"></div>
    <ul><li>Terms of Use</li><li>Site Map</li><li>Privacy Policy</li><li>Resources</li><li>Our Clients</li><li>News &amp; Events</li><li>Contact Us</li></ul>
  </div>
  <div class="fcol" style="left:610px">
    <h4>Contact Info</h4><div class="bar"></div>
    <div class="ci"><svg width="12" height="16" viewBox="0 0 12 16"><path fill="#ee7d30" d="M6 0a6 6 0 0 0-6 6c0 4.5 6 10 6 10s6-5.5 6-10a6 6 0 0 0-6-6zm0 8.5A2.5 2.5 0 1 1 6 3.5a2.5 2.5 0 0 1 0 5z"/></svg><div><b>Address</b>Lorem Ipsum has been the industry's<br>standard dummy text ever since.</div></div>
    <div class="ci"><svg width="13" height="13" viewBox="0 0 24 24"><path fill="#ee7d30" d="M6.6 10.8c1.4 2.8 3.8 5.1 6.6 6.6l2.2-2.2c.3-.3.7-.4 1-.2 1.1.4 2.3.6 3.6.6.6 0 1 .4 1 1V20c0 .6-.4 1-1 1C10.6 21 3 13.4 3 4c0-.6.4-1 1-1h3.5c.6 0 1 .4 1 1 0 1.3.2 2.5.6 3.6.1.3 0 .7-.2 1z"/></svg><div><b>Phone</b>US &nbsp; +1 555.014.2290<br>UK &nbsp; +44 (0) 7700 900418</div></div>
    <div class="ci" style="border:none"><svg width="14" height="11" viewBox="0 0 14 11"><rect width="14" height="11" rx="1" fill="#ee7d30"/><path d="M1 1l6 5 6-5" stroke="#262626" stroke-width="1.2" fill="none"/></svg><div><b>Email</b>info@boldharbor.com</div></div>
  </div>
  <div class="fcol news" style="left:848px">
    <h4>Newsletter</h4><div class="bar"></div>
    <p>Lorem Ipsum has been the industry's</p>
    <div class="mail">Enter Your Email Here... <svg width="22" height="10" viewBox="0 0 22 10"><path d="M0 5h20M15 1l5 4-5 4" stroke="#ee7d30" stroke-width="1.6" fill="none"/></svg></div>
    <div class="socials"><span>Kite</span><span>Loop</span><span>Chirp</span></div>
  </div>
  <div class="fline"></div>
  <div class="copy abs center">© 2021 Bold Harbor | LEADING WITH CLARITY Since 2021</div>
</footer>

</body>
</html>
```